Lorn Systems

Looking for a web site design to market our services/applications
We write and supply bespoke web applications for the offshore and construction industries
Our initial product is Velk - rope access equipment management
Our buyers will be Rope Access companies via trade associations such as OBWEN and KLUDE
we have a logo designed see it attached we would like to see crisp professional designs based around these colours and design
we will supply web copy later
looking for home, services, blog, contact us, order and a general template (privacy, site map, T&C) pages
Updates
This payment will be for the homepage only
We can discuss other options (pages) with the successful designer
Regards
Brian
Industry/Entity Type
Construction
Look and feel
Each slider illustrates characteristics of the customer's brand and the style your logo design should communicate.

```html
<!DOCTYPE html>
<html lang="en">
<head>
<meta charset="utf-8">
<title>Lorn Systems</title>
<link href="https://fonts.googleapis.com/css2?family=Oswald:wght@400;500&family=Roboto:wght@400;500;700&display=swap" rel="stylesheet">
<style>
:root{
  --page:#f1f1f1;
  --navy:#2a2b8f;
  --sky:#0ea5e6;
  --sky-light:#6fcff3;
  --ink:#222;
  --rule:#9a9a9a;
  --footer:#262626;
  --tile:#e6e6e6;
}
*{margin:0;padding:0;box-sizing:border-box}
html,body{width:918px;height:1200px;overflow:hidden;background:var(--page);font-family:'Roboto',sans-serif;color:var(--ink)}
.canvas{position:relative;width:918px;height:1200px}
.abs{position:absolute}

.brand{left:49px;top:18px;display:flex;align-items:center;gap:14px}
.brand-mark{width:54px;height:54px;border-radius:6px;background:var(--navy)}
.brand-rule{width:1px;height:76px;background:#ccc}
.brand-name{font-family:'Roboto',sans-serif;font-weight:500;font-size:22px;color:var(--navy);line-height:1}

.help-bubble{left:528px;top:7px;width:30px;height:24px;border-radius:50%;background:var(--sky);color:#fff;font-size:9px;font-weight:700;display:flex;align-items:center;justify-content:center}
.help-bar{left:562px;top:19px;width:176px;height:23px;background:var(--navy);color:#fff;font-size:11px;display:flex;align-items:center;justify-content:center;gap:3px}
.help-bar b{font-weight:700}
.social{left:742px;top:19px;display:flex;gap:4px}
.social span{width:40px;height:23px;background:var(--navy);color:#fff;font-size:10px;display:flex;align-items:center;justify-content:center}

.nav{left:470px;top:53px;width:398px;height:27px;background:var(--sky);display:flex;align-items:center;justify-content:space-between;padding:0 12px;font-family:'Oswald',sans-serif;font-size:12px}
.nav a{color:var(--navy);text-decoration:none}
.nav a.current{color:#fff}

.slider{left:49px;top:104px;width:819px;height:264px;border:1px solid #ccc;background:linear-gradient(135deg,#1d3d6e 0%,#3a6d9c 40%,#b7c9d6 60%,#5b6e80 100%)}
.slide-caption{left:191px;top:285px;width:390px;height:50px;background:rgba(40,40,40,.82);color:#fff;font-family:'Oswald',sans-serif;font-size:25px;display:flex;align-items:center;padding-left:10px}
.dots{left:433px;top:377px;display:flex;gap:6px}
.dots i{width:8px;height:8px;background:var(--sky-light)}
.dots i.on{background:var(--navy)}

.feature{top:416px;width:250px;text-align:center}
.feature-circle{width:108px;height:108px;border-radius:50%;background:#fff;margin:0 auto;display:flex;align-items:center;justify-content:center}
.feature h2{font-family:'Oswald',sans-serif;font-weight:400;font-size:22px;color:var(--sky);margin-top:8px;line-height:28px}
.feature p{font-size:11.5px;line-height:14.5px;margin-top:1px}
.btn{display:inline-block;margin-top:7px;background:var(--navy);color:#fff;font-size:11.5px;width:74px;height:22px;line-height:22px}

.section-head{left:49px;width:819px;display:flex;align-items:center;gap:8px;font-family:'Oswald',sans-serif;font-size:23px;color:var(--navy)}
.section-head span{color:var(--sky)}
.section-head .line{flex:1;height:1px;background:var(--rule);margin-top:4px}

.laptop{left:49px;top:738px;width:257px;height:162px;border-radius:6px;background:linear-gradient(160deg,#2b2b2b 0%,#e9e9e9 55%,#b9b9b9 100%)}
.welcome-text{left:329px;top:725px;width:538px;font-size:10.4px;line-height:15.9px}
.welcome-text p+p{margin-top:15.9px}

.tile{top:982px;width:126px;height:88px;background:var(--tile);border:2px solid #fff;display:flex;align-items:center;justify-content:center;font-family:'Roboto',sans-serif;font-weight:700;font-size:20px;color:#1a1a2e}

.footer{left:49px;top:1100px;width:819px;height:100px;background:var(--footer);color:#fff}
.f-col{position:absolute;top:20px;display:flex;gap:10px;font-size:9.6px;line-height:15px}
.f-col h3{font-family:'Oswald',sans-serif;font-weight:400;font-size:12.5px;line-height:16px}
.f-social{display:flex;gap:10px;margin-top:2px;font-size:9.6px}
</style>
</head>
<body>
<div class="canvas">

  <div class="abs brand">
    <div class="brand-mark"></div>
    <div class="brand-rule"></div>
    <div class="brand-name">Lorn Systems</div>
  </div>

  <div class="abs help-bubble">24/7</div>
  <div class="abs help-bar"><b>Need Help?</b> Call Us 000-000-0000</div>
  <div class="abs social"><span>Share</span><span>Post</span><span>Join</span></div>

  <nav class="abs nav">
    <a class="current" href="#">Home</a><a href="#">Services</a><a href="#">Blog</a><a href="#">Order</a><a href="#">Privacy</a><a href="#">Contact Us</a>
  </nav>

  <div class="abs slider" role="img" aria-label="Rope access technician working at height beside a desktop computer showing a software screenshot"></div>
  <div class="abs slide-caption">ROPE ACCESS EQUIPMENT MANAGEMENT</div>
  <div class="abs dots"><i></i><i class="on"></i><i></i><i></i></div>

  <div class="abs feature" style="left:39px">
    <div class="feature-circle">
      <svg width="66" height="66" viewBox="0 0 66 66"><rect x="2" y="26" width="11" height="36" rx="4" fill="var(--navy)"/><path d="M18 30 L30 12 Q34 2 40 8 Q42 14 38 24 L58 24 Q64 26 62 34 L58 56 Q56 62 48 62 L22 62 Q18 62 18 58 Z" fill="none" stroke="var(--navy)" stroke-width="7" stroke-linejoin="round"/></svg>
    </div>
    <h2>EASY TO USE</h2>
    <p>Lorem Ipsum is simply dummy text of the printing and typesetting industry. Lorem Ipsum has been</p>
    <span class="btn">Read more</span>
  </div>

  <div class="abs feature" style="left:334px">
    <div class="feature-circle">
      <svg width="56" height="66" viewBox="0 0 56 66"><path d="M8 18 Q10 4 28 4 Q48 4 48 20 Q48 30 36 36 Q32 39 32 46 L22 46 Q22 34 30 29 Q38 25 37 20 Q36 13 28 13 Q20 13 19 21 Z" fill="var(--navy)"/><rect x="21" y="52" width="12" height="12" fill="var(--navy)"/></svg>
    </div>
    <h2>INSTANT HELP</h2>
    <p>Lorem Ipsum is simply dummy text of the printing and typesetting industry. Lorem Ipsum has been</p>
    <span class="btn">Read more</span>
  </div>

  <div class="abs feature" style="left:627px">
    <div class="feature-circle">
      <svg width="66" height="66" viewBox="-33 -33 66 66">
        <g fill="var(--navy)">
          <rect x="-7" y="-32" width="14" height="64" rx="2"/>
          <rect x="-7" y="-32" width="14" height="64" rx="2" transform="rotate(45)"/>
          <rect x="-7" y="-32" width="14" height="64" rx="2" transform="rotate(90)"/>
          <rect x="-7" y="-32" width="14" height="64" rx="2" transform="rotate(135)"/>
          <circle r="23"/>
        </g>
        <circle r="10" fill="#fff"/>
      </svg>
    </div>
    <h2>COOL SETTINGS</h2>
    <p>Lorem Ipsum is simply dummy text of the printing and typesetting industry. Lorem Ipsum has been</p>
    <span class="btn">Read more</span>
  </div>

  <div class="abs section-head" style="top:679px">Welcome to <span>Lorn Systems</span><i class="line"></i></div>

  <div class="abs laptop" role="img" aria-label="Laptop showing a software screenshot"></div>
  <div class="abs welcome-text">
    <p>There are many variations of passages of Lorem Ipsum available, but the majority have suffered alteration in some form, by injected humour, or randomised words which don't look even slightly believable. If you are going to use a passage of Lorem Ipsum, you need to be sure there isn't anything embarrassing hidden in the middle of text. All the Lorem Ipsum generators on the Internet tend to repeat predefined chunks as necessary, making this the first true generator on the Internet. It uses a dictionary of over 200 Latin words, combined with a handful of model sentence structures, to generate Lorem Ipsum which looks reasonable. The generated Lorem Ipsum is therefore always free from repetition, injected humour, or non-characteristic words etc.</p>
    <p>It is a long established fact that a reader will be distracted by the readable content of a page when looking at its layout. The point of using Lorem Ipsum is that it has a more-or-less normal distribution of letters, as opposed to using.</p>
  </div>

  <div class="abs section-head" style="top:940px">Our <span>Clent</span><i class="line"></i></div>

  <div class="abs tile" style="left:48px">KLUDE</div>
  <div class="abs tile" style="left:185px">OBWEN</div>
  <div class="abs tile" style="left:323px">KLUDE</div>
  <div class="abs tile" style="left:463px">OBWEN</div>
  <div class="abs tile" style="left:602px">KLUDE</div>
  <div class="abs tile" style="left:741px">OBWEN</div>

  <footer class="abs footer">
    <div class="f-col" style="left:17px">
      <svg width="20" height="28" viewBox="0 0 20 28"><path d="M10 0 Q20 0 20 10 Q20 17 10 28 Q0 17 0 10 Q0 0 10 0 Z" fill="#fff"/><circle cx="10" cy="10" r="3.5" fill="var(--footer)"/></svg>
      <div><h3>Address</h3>Lorem Ipsum used since the 1500s<br>is reproduced below for those</div>
    </div>
    <div class="f-col" style="left:232px">
      <svg width="20" height="28" viewBox="0 0 20 28"><path d="M4 2 L8 1 L10 8 L7 10 Q7 16 11 20 L14 18 L19 23 L16 27 Q2 24 1 8 Z" fill="#fff"/></svg>
      <div><h3>Call</h3><b>T -</b> 000 - 0000 - 0000<br><b>F -</b> 000 - 0000 - 0000</div>
    </div>
    <div class="f-col" style="left:421px">
      <svg width="36" height="22" viewBox="0 0 36 22"><rect x="1" y="1" width="34" height="20" fill="none" stroke="#fff" stroke-width="2"/><path d="M1 1 L18 13 L35 1 M1 21 L14 10 M35 21 L22 10" fill="none" stroke="#fff" stroke-width="2"/></svg>
      <div><h3>Contact</h3><b>E -</b> hello@lornsystems.test<div class="f-social"><span>Share</span><span>Post</span><span>Join</span></div></div>
    </div>
    <div class="f-col" style="left:649px;top:28px">
      <svg width="22" height="22" viewBox="0 0 22 22"><circle cx="11" cy="11" r="9.5" fill="none" stroke="#fff" stroke-width="2"/><path d="M14.5 8 Q13 6 11 6 Q6 6 6 11 Q6 16 11 16 Q13 16 14.5 14" fill="none" stroke="#fff" stroke-width="2"/></svg>
      <div>© 2014 by Lorn Systems.</div>
    </div>
  </footer>

</div>
</body>
</html>
```